依頼詳細
12月の年末繁忙期に合わせて、新聞折込を実施する予定です。ただ、おコメの麺の説明が難しく消費者には伝わりにくいため、純粋にちゃんぽんや台湾風まぜそばを全面に打ち出して当社に来店してもらい、結果的に米粉麺だったくらいの主張でいいと思っています。チラシの下部に100円キャッシュバック券をつけたいと考えています。(期限は2023年2月末)
記載項目
こむぎ茶屋 しずくや みずほ灯籠館店 (道の駅みずほ灯籠館内フードコート)
住所 長岡市桜井町318 TEL090-6978-5739
営業時間10:00~19:00

とろみちゃんぽん 880円
とろみちゃんぽん旨辛味噌のせ 910円
台湾風まぜそば 910円
サイズ
A4
ページ数
片面
希望イメージ
シンプル 複雑
単色 カラフル
暗い 明るい
日常 高級
遊び心 厳粛
未来的 伝統的
女性的 男性的
希望する色
黄・オレンジ系
納品ファイル
• 高解像度JPG (.jpg)

はじめてみた人が感じるインパクトがあり、色彩もよかったです。

毎回たくさんの応募ありがとうございます。
結果的に非常に満足しておりますので、これからも依頼したいと思います。
よろしくお願いします。

```html
<!DOCTYPE html>
<html lang="ja">
<head>
<meta charset="utf-8">
<title>しずくや 折込チラシ</title>
<link href="https://fonts.googleapis.com/css2?family=M+PLUS+Rounded+1c:wght@800;900&family=Noto+Sans+JP:wght@400;700;900&display=swap" rel="stylesheet">
<style>
:root{
  --bg-top:#fbd64a;
  --bg-bottom:#f6b51e;
  --orange:#ef7d14;
  --red:#d8261b;
  --ink:#2a1a0c;
  --white:#ffffff;
  --cream:#fff7e0;
  --gold:#ffe46a;
}
*{margin:0;padding:0;box-sizing:border-box}
html,body{width:849px;height:1200px;overflow:hidden}
body{font-family:"Noto Sans JP",sans-serif;color:var(--ink)}
.flyer{position:relative;width:849px;height:1200px;overflow:hidden;
  background:linear-gradient(180deg,var(--bg-top) 0%,var(--bg-bottom) 100%)}
.abs{position:absolute}
.lead{top:0;left:0;width:100%;height:46px;background:var(--orange);color:var(--white);
  font-weight:700;font-size:19px;text-align:center;line-height:46px;letter-spacing:.04em}
.photo{border-radius:50%;box-shadow:0 6px 18px rgba(120,60,0,.25)}
.photo-champon{left:-40px;top:50px;width:420px;height:360px;
  background:radial-gradient(circle at 50% 45%,#fbf3e2 0%,#efdcb8 45%,#c9a06a 75%,#7a4e25 100%)}
.photo-closeup{left:657px;top:113px;width:170px;height:160px;border:5px solid var(--white);
  background:radial-gradient(circle at 45% 45%,#fffaf0 0%,#f0e2c4 60%,#c79a5e 100%)}
.photo-mazesoba{left:500px;top:470px;width:380px;height:360px;
  background:radial-gradient(circle at 50% 45%,#d07b2c 0%,#8c4b1b 50%,#3e2412 100%)}
.photo-miso{left:-40px;top:555px;width:520px;height:330px;
  background:radial-gradient(circle at 50% 45%,#f6eee0 0%,#e7cfa4 45%,#c9733a 75%,#6e3b1a 100%)}
.label{background:var(--ink);color:var(--white);font-weight:900;padding:3px 14px;font-size:26px;letter-spacing:.05em;line-height:1.35}
.price{font-size:17px;color:var(--gold);margin-left:8px;letter-spacing:0}
.label-a{left:372px;top:60px}
.catch{color:var(--red);font-weight:900;font-size:24px}
.catch-a{left:378px;top:108px}
.desc{font-size:17px;font-weight:700;line-height:1.5}
.desc-a{left:378px;top:142px}
.closeup-note{left:640px;top:285px;width:200px;text-align:center;font-weight:900;font-size:18px;color:var(--red);line-height:1.3}
.headline{left:60px;top:352px;width:760px;transform:rotate(-4deg);text-align:center;
  font-family:"M PLUS Rounded 1c",sans-serif;font-weight:900;color:var(--white);
  -webkit-text-stroke:3px var(--red);paint-order:stroke fill;text-shadow:4px 5px 0 var(--red)}
.headline .line1{display:block;font-size:78px;line-height:1.15}
.headline .line2{display:block;font-size:80px;line-height:1.15}
.label-b{left:510px;top:640px}
.desc-b{left:500px;top:694px;width:340px;color:var(--white);text-shadow:0 1px 3px rgba(0,0,0,.6)}
.desc-b .catch{color:var(--gold);font-size:20px}
.label-c{left:28px;top:880px;font-size:25px}
.catch-c{left:32px;top:962px;font-size:22px}
.desc-c{left:32px;top:994px;font-size:16px;line-height:1.45}
.coupon{left:488px;top:880px;width:352px;height:126px;background:var(--white);
  border:3px dashed var(--orange);padding:10px 14px}
.coupon .shop{font-size:13px;font-weight:700}
.coupon .amount{position:absolute;left:118px;top:34px;font-size:56px;font-weight:900;color:var(--red);line-height:1}
.coupon .yen{font-size:34px}
.coupon .kind{position:absolute;right:10px;top:30px;writing-mode:vertical-rl;background:var(--red);color:var(--white);
  font-weight:900;font-size:12px;line-height:1.2;padding:5px 3px;height:84px}
.coupon .limit{position:absolute;left:14px;bottom:8px;font-size:13px;font-weight:700}
.coupon .mark{position:absolute;left:18px;top:44px;width:80px;height:40px;border:2px solid var(--red);
  color:var(--red);font-weight:900;font-size:16px;text-align:center;line-height:36px}
.footer{left:0;top:1050px;width:849px;height:150px;background:var(--cream)}
.brand{left:28px;top:1060px;display:flex;align-items:center;gap:10px;font-weight:900;font-size:30px;line-height:1.2}
.brand .dot{width:26px;height:26px;background:var(--orange);border-radius:50%}
.brand small{font-size:14px;display:block;font-weight:900}
.store{left:300px;top:1058px;font-weight:900;font-size:24px;line-height:1.3}
.contact{left:300px;top:1092px;font-size:16px;font-weight:700;line-height:1.5}
.contact svg{vertical-align:-3px;margin-right:4px}
.address{left:28px;top:1146px;font-size:12px;line-height:1.4;width:560px}
.map{left:600px;top:1060px;width:240px;height:130px;border:2px solid var(--orange);
  background:linear-gradient(135deg,#f4efe2,#e4dcc6)}
</style>
</head>
<body>
<div class="flyer">
  <div class="abs lead">新潟産米を使用した、のどごし自慢の麺をご賞味ください！</div>

  <div class="abs photo photo-champon" role="img" aria-label="野菜たっぷりのとろみちゃんぽんの写真"></div>
  <div class="abs label label-a">とろみちゃんぽん<span class="price">880円</span></div>
  <div class="abs catch catch-a">国産野菜たっぷり</div>
  <div class="abs desc desc-a">香ばしいスープと麺の食感が<br>奏でるハーモニー</div>

  <div class="abs photo photo-closeup" role="img" aria-label="つややかな白い米粉麺を箸で持ち上げた写真"></div>
  <div class="abs closeup-note">独自製法の<br>ツルモチ食感！</div>

  <div class="abs photo photo-mazesoba" role="img" aria-label="台湾風まぜそばの写真"></div>
  <div class="abs photo photo-miso" role="img" aria-label="旨辛味噌をのせたとろみちゃんぽんの写真"></div>

  <h1 class="abs headline"><span class="line1">つるつるもちもちの</span><span class="line2">白く輝くおコメの麺</span></h1>

  <div class="abs label label-b">台湾風まぜそば<span class="price">910円</span></div>
  <div class="abs desc desc-b"><span class="catch">混ぜれば混ぜるほどうまくなる</span><br>米の甘みと具材の旨みが<br>重なり合う凝縮した旨味</div>

  <div class="abs label label-c">とろみちゃんぽん<br>旨辛味噌のせ<span class="price">910円</span></div>
  <div class="abs catch catch-c">旨味と辛みの絶妙なバランス</div>
  <div class="abs desc desc-c">旨辛味噌の辛さと凝縮された<br>旨味が絡み合う</div>

  <div class="abs coupon">
    <div class="shop">こむぎ茶屋 しずくや　みずほ灯籠館店</div>
    <div class="mark">ご提示</div>
    <div class="amount"><span class="yen">¥</span>100</div>
    <div class="kind">キャッシュバック</div>
    <div class="limit">有効期限：2023年2月末</div>
  </div>

  <div class="abs footer"></div>
  <div class="abs brand"><span class="dot"></span><div><small>こむぎ茶屋</small>しずくや</div></div>
  <div class="abs store">みずほ灯籠館店</div>
  <div class="abs contact">
    <svg width="16" height="16" viewBox="0 0 16 16"><path d="M3 1h3l1 4-2 1c1 2 3 4 5 5l1-2 4 1v3c0 1-1 2-2 2C7 15 1 9 1 3c0-1 1-2 2-2z" fill="#ef7d14"/></svg>TEL 090-4213-8062<br>
    営業時間 10:00～19:00
  </div>
  <div class="abs address">長岡市桜井町318（道の駅みずほ灯籠館内フードコート）<br>※ 駐車場は道の駅の無料駐車場をご利用ください<br>※ 道の駅みずほ灯籠館の休館日は休業となります</div>
  <div class="abs map" role="img" aria-label="道の駅みずほ灯籠館周辺の地図"></div>
</div>
</body>
</html>
```